ORLU Facility Services ball field sign

Hello all!
I have bought a 4x6 sign space at our local Cobble Meadow baseball field. This sign space will be used to display a sign for ORLU Facility Services. The color, font and logos are located in the files attached. May accept the following on the sign: “HVAC · Refrigeration · Plumbing · Electrical · Commercial Cooking Equipment”. I would maybe like to see some designs that match our van rap style. Another slogan we use sometimes is “ One Call. Every Trade. Every Time.” QR Code could be used to schedule service.

Target Market(s)

Commercial Customers

Industry/Entity Type

Commercial Facility Services

Requirements
Must have
• Phone: 518.627.3395; WEB: www.ORLUFS.example
Should not have
• Do not mention anything related to county or park on the sign

```html
<!DOCTYPE html>
<html lang="en">
<head>
<meta charset="utf-8">
<title>ORLU Facility Services – Ball Field Sign Options</title>
<link rel="stylesheet" href="https://fonts.googleapis.com/css2?family=Oswald:wght@600;700&family=Poppins:wght@600;700&display=swap">
<style>
  :root {
    --brand-blue: #0f47a2;
    --white: #ffffff;
    --board: #444444;
    --steel-dark: #a6b7bd;
    --steel-light: #d8dadb;
  }
  * { margin: 0; padding: 0; box-sizing: border-box; }
  html, body { width: 1200px; height: 908px; overflow: hidden; background: var(--board); }
  .board { position: relative; width: 1200px; height: 908px; }
  .sign {
    position: absolute; width: 456px; height: 304px;
    background: var(--white); overflow: hidden;
    font-family: "Poppins", sans-serif;
  }
  .sign--a { left: 126px; top: 134px; }
  .sign--b { left: 618px; top: 134px; }
  .sign--c { left: 126px; top: 475px; }
  .sign--d { left: 618px; top: 475px; }
  .sign svg.backdrop { position: absolute; inset: 0; width: 456px; height: 304px; }
  .sign .txt { position: absolute; white-space: nowrap; line-height: 1; }

  .brand { font-family: "Poppins", sans-serif; font-weight: 700; font-size: 38px; letter-spacing: 3px; transform: translate(-50%, -50%); }
  .brand--blue { color: var(--brand-blue); }
  .brand--white { color: var(--white); }

  .services { left: 0; width: 456px; text-align: center; font-weight: 600; font-size: 16.5px; }
  .phone { left: 0; width: 456px; text-align: center; font-weight: 700; font-size: 42px; letter-spacing: 0.5px; transform: translateY(-50%); }
  .web { left: 0; width: 456px; text-align: center; font-weight: 700; font-size: 19px; transform: translateY(-50%); color: var(--white); }
  .on-blue { color: var(--white); }
  .on-white { color: var(--brand-blue); }

  .slogan-condensed { right: 24px; text-align: right; font-family: "Oswald", sans-serif; font-weight: 600; font-size: 39px; line-height: 46px; color: var(--white); }
  .phone-condensed { right: 24px; font-family: "Oswald", sans-serif; font-weight: 700; font-size: 44px; color: var(--white); transform: translateY(-50%); }
  .web-right { right: 24px; font-weight: 700; font-size: 18px; color: var(--white); transform: translateY(-50%); }
  .slogan-caps { right: 25px; text-align: right; font-weight: 700; font-size: 23px; line-height: 33px; color: var(--white); }
</style>
</head>
<body>
<div class="board">

  <!-- Option A: white header, blue body -->
  <section class="sign sign--a">
    <svg class="backdrop" viewBox="0 0 456 304" aria-hidden="true">
      <defs>
        <linearGradient id="steelA" x1="0" x2="1" y1="0" y2="0">
          <stop offset="0" stop-color="#a6b7bd"/><stop offset="0.5" stop-color="#d8dadb"/><stop offset="1" stop-color="#a6b7bd"/>
        </linearGradient>
      </defs>
      <path d="M0,83 Q228,135 456,83 L456,304 L0,304 Z" fill="url(#steelA)"/>
      <path d="M0,87 Q228,177 456,87 L456,304 L0,304 Z" fill="#0f47a2"/>
    </svg>
    <div class="txt brand brand--blue" style="left:218px; top:59px;">ORLU</div>
    <div class="txt services on-blue" style="top:147px;">HVAC · Refrigeration · Plumbing · Electrical</div>
    <div class="txt services on-blue" style="top:170px;">· Commercial Cooking Equipment</div>
    <div class="txt phone on-blue" style="top:227px;">518.627.3395</div>
    <div class="txt web" style="top:277px;">www.ORLUFS.example</div>
  </section>

  <!-- Option B: diagonal blue panel with slogan -->
  <section class="sign sign--b">
    <svg class="backdrop" viewBox="0 0 456 304" aria-hidden="true">
      <defs>
        <linearGradient id="steelB" x1="0" x2="1" y1="1" y2="0">
          <stop offset="0" stop-color="#a6b7bd"/><stop offset="0.55" stop-color="#d8dadb"/><stop offset="1" stop-color="#b9c6ca"/>
        </linearGradient>
      </defs>
      <polygon points="0,304 184,103 61,304" fill="url(#steelB)"/>
      <polygon points="61,304 184,103 117,304" fill="#a6b7bd"/>
      <polygon points="220,0 456,0 456,304 117,304" fill="#0f47a2"/>
    </svg>
    <div class="txt brand brand--blue" style="left:91px; top:58px; font-size:34px;">ORLU</div>
    <div class="txt slogan-condensed" style="top:18px;">One Call.<br>Every Trade.<br>Every Time.</div>
    <div class="txt phone-condensed" style="top:216px;">518.627.3395</div>
    <div class="txt web-right" style="top:262px;">www.ORLUFS.example</div>
  </section>

  <!-- Option C: blue header, white body, web tab -->
  <section class="sign sign--c">
    <svg class="backdrop" viewBox="0 0 456 304" aria-hidden="true">
      <defs>
        <linearGradient id="steelC" x1="0" x2="1" y1="0" y2="0">
          <stop offset="0" stop-color="#a6b7bd"/><stop offset="0.5" stop-color="#d8dadb"/><stop offset="1" stop-color="#a6b7bd"/>
        </linearGradient>
      </defs>
      <path d="M0,0 L456,0 L456,86 Q228,170 0,86 Z" fill="url(#steelC)"/>
      <path d="M0,0 L456,0 L456,81 Q228,131 0,81 Z" fill="#0f47a2"/>
      <path d="M60,304 L95,262 Q101,258 115,258 L340,258 Q358,258 370,268 L392,304 Z" fill="#0f47a2"/>
    </svg>
    <div class="txt brand brand--white" style="left:228px; top:53px;">ORLU</div>
    <div class="txt services on-white" style="top:146px;">HVAC · Refrigeration · Plumbing · Electrical</div>
    <div class="txt services on-white" style="top:169px;">· Commercial Cooking Equipment</div>
    <div class="txt phone on-white" style="top:224px;">518.627.3395</div>
    <div class="txt web" style="top:282px;">www.ORLUFS.example</div>
  </section>

  <!-- Option D: blue wave header with slogan -->
  <section class="sign sign--d">
    <svg class="backdrop" viewBox="0 0 456 304" aria-hidden="true">
      <defs>
        <linearGradient id="steelD" x1="0" x2="1" y1="0" y2="0">
          <stop offset="0" stop-color="#a6b7bd"/><stop offset="0.55" stop-color="#d8dadb"/><stop offset="1" stop-color="#a6b7bd"/>
        </linearGradient>
      </defs>
      <path d="M0,0 L456,0 L456,133 C400,140 320,144 230,142 C150,138 80,130 0,143 Z" fill="url(#steelD)"/>
      <path d="M0,0 L456,0 L456,120 C400,128 320,132 230,124 C160,116 70,104 0,124 Z" fill="#0f47a2"/>
      <path d="M60,304 L95,262 Q101,258 115,258 L340,258 Q358,258 370,268 L392,304 Z" fill="#0f47a2"/>
    </svg>
    <div class="txt brand brand--white" style="left:97px; top:55px;">ORLU</div>
    <div class="txt slogan-caps" style="top:16px;">ONE CALL.<br>EVERY TRADE.<br>EVERY TIME.</div>
    <div class="txt services on-white" style="top:155px;">HVAC · Refrigeration · Plumbing · Electrical</div>
    <div class="txt services on-white" style="top:178px;">· Commercial Cooking Equipment</div>
    <div class="txt phone on-white" style="top:228px;">518.627.3395</div>
    <div class="txt web" style="top:279px;">www.ORLUFS.example</div>
  </section>

</div>
</body>
</html>
```